Résumé app needs 1 more template

Hi, I need 1 more template for my résumé app. The résumé app can be used in a browser (https://brightquill.com/resume-app) on an Koravo / Tabrix (https://apps.orvantel.com/app/id583726104) or on an Vellumos (https://market.tindrel.com/store/apps/details?id=com.brightquill.resume). The app lets the user create a résumé. It currently let's the user choose between 3 templates. I need 1 more. Please use the app first so you know how it will work.

Reason: Need more designs

Target Market(s)

Users of the app

Colors

Designer to choose colors to be used in the design.

Requirements
Must have
• original
• beautiful
• the resume template contains the data that the user can currently enter in the app (so do NOT design new features like sliders for level of experience etc)

```html
<!DOCTYPE html>
<html lang="en">
<head>
<meta charset="utf-8">
<title>Résumé Template – John Doe</title>
<link rel="stylesheet" href="https://fonts.googleapis.com/css2?family=Raleway:wght@400;500;600;700;800&display=swap">
<style>
  :root {
    --teal: #53bcd3;
    --blue: #547cd4;
    --bar-blue: #6888dd;
    --bar-teal: #52bbd3;
    --ink: #222428;
    --ink-soft: #444850;
    --white: #ffffff;
    --canvas: #ffffff;
  }
  * { box-sizing: border-box; margin: 0; padding: 0; }
  html, body {
    width: 1200px; height: 1200px; overflow: hidden;
    background: var(--canvas);
    font-family: "Raleway", sans-serif;
    color: var(--ink);
  }
  .resume {
    position: absolute; left: 230px; top: 77px;
    width: 739px; height: 1046px;
    background: var(--white);
    box-shadow: 0 10px 40px rgba(0,0,0,0.12);
    overflow: hidden;
  }
  .abs { position: absolute; }

  /* Header */
  .header {
    left: 18px; top: 0; width: 707px; height: 201px;
    background: var(--teal);
    border-radius: 0 0 80px 80px;
    color: var(--white);
  }
  .greeting { left: 51px; top: 30px; font-size: 18px; font-weight: 700; }
  .name { left: 33px; top: 50px; font-size: 74px; font-weight: 700; letter-spacing: -1px; line-height: 1; }
  .contact { left: 452px; top: 48px; list-style: none; font-size: 15px; font-weight: 500; }
  .contact li { display: flex; align-items: center; height: 24px; }
  .contact svg { width: 14px; height: 14px; margin-right: 9px; fill: var(--white); }
  .dots { left: 32px; top: 129px; width: 640px; border-top: 3px dotted rgba(255,255,255,0.9); }
  .intro { left: 20px; top: 142px; width: 667px; text-align: center; font-size: 12px; line-height: 16px; }

  /* Section headings */
  .heading { font-size: 18px; font-weight: 700; color: var(--ink); }
  .heading.lg { font-size: 21px; }

  /* Qualifications */
  .qual-group { font-size: 14.5px; color: var(--ink-soft); }
  .col-label { width: 110px; margin-left: -55px; text-align: center; font-size: 12.5px; line-height: 16px; color: var(--ink-soft); }
  .bar { width: 99px; height: 18px; }
  .bar.blue { background: var(--bar-blue); }
  .bar.teal { background: var(--bar-teal); }

  /* Skills */
  .skill { font-size: 12.5px; color: var(--ink); }

  /* Referees */
  .ref-label { font-size: 12.5px; color: var(--ink); }
  .ref-line { width: 146px; border-top: 1px dashed var(--ink-soft); }

  /* Panels */
  .about {
    left: 10px; top: 522px; width: 286px; height: 524px;
    background: var(--blue);
    border-radius: 64px 64px 0 0;
    color: var(--white);
  }
  .interests {
    left: 296px; top: 759px; width: 434px; height: 287px;
    background: var(--teal);
    border-radius: 0 64px 64px 0;
    color: var(--white);
  }
  .panel-heading { font-size: 21px; font-weight: 700; line-height: 26px; color: var(--white); }
  .panel-text { font-size: 13px; line-height: 16px; font-weight: 500; }
  .experience { list-style: none; width: 198px; }
  .experience li { font-size: 13.5px; height: 37px; padding-top: 0; border-bottom: 1px dashed rgba(255,255,255,0.85); margin-bottom: 0; line-height: 18px; }
</style>
</head>
<body>
<main class="resume">

  <header class="header abs">
    <p class="greeting abs">Hi my name is</p>
    <h1 class="name abs">JOHN DOE</h1>
    <ul class="contact abs">
      <li><svg viewBox="0 0 24 24"><path d="M6.6 10.8a15.1 15.1 0 0 0 6.6 6.6l2.2-2.2a1 1 0 0 1 1-.25 11.4 11.4 0 0 0 3.6.57 1 1 0 0 1 1 1V20a1 1 0 0 1-1 1A17 17 0 0 1 3 4a1 1 0 0 1 1-1h3.5a1 1 0 0 1 1 1c0 1.25.2 2.45.57 3.57a1 1 0 0 1-.25 1z"/></svg>123 456 7890</li>
      <li><svg viewBox="0 0 24 24"><path d="M2 5h20v14H2z M3.5 6.5 12 13l8.5-6.5" fill="none" stroke="#fff" stroke-width="2"/></svg>yourname@mailnest.com</li>
      <li><svg viewBox="0 0 24 24"><rect x="3" y="3" width="18" height="18" rx="2"/></svg>linkvane.com/yourprofile</li>
    </ul>
    <div class="dots abs"></div>
    <p class="intro abs">Lorem Ipsum is simply dummy text of the printing and typesetting industry. Lorem Ipsum has been the industry's standard dummy text ever since the 1500s, when an unknown printer took a galley of type and scrambled.</p>
  </header>

  <!-- Qualifications -->
  <h2 class="heading abs" style="left:46px;top:226px;">QUALIFICATIONS</h2>

  <p class="qual-group abs" style="left:47px;top:267px;">Qualifications 1</p>
  <p class="col-label abs" style="left:96px;top:298px;">Qualification<br>title</p>
  <p class="col-label abs" style="left:216px;top:298px;">Institution</p>
  <p class="col-label abs" style="left:336px;top:298px;">Year<br>completed</p>
  <div class="bar blue abs" style="left:46px;top:338px;"></div>
  <div class="bar teal abs" style="left:166px;top:338px;"></div>
  <div class="bar blue abs" style="left:286px;top:338px;"></div>

  <p class="qual-group abs" style="left:46px;top:380px;">Qualifications 2</p>
  <p class="col-label abs" style="left:96px;top:412px;">Qualification<br>title</p>
  <p class="col-label abs" style="left:216px;top:412px;">Institution</p>
  <p class="col-label abs" style="left:336px;top:412px;">Year<br>completed</p>
  <div class="bar teal abs" style="left:46px;top:453px;"></div>
  <div class="bar blue abs" style="left:166px;top:453px;"></div>
  <div class="bar teal abs" style="left:286px;top:453px;"></div>

  <!-- Skills -->
  <h2 class="heading abs" style="left:432px;top:226px;">SKILLS</h2>
  <p class="skill abs" style="left:434px;top:258px;">• Skill 1 goes here</p>
  <p class="skill abs" style="left:434px;top:284px;">• Skill 2 goes here</p>
  <p class="skill abs" style="left:434px;top:310px;">• Skill 3 goes here</p>
  <p class="skill abs" style="left:434px;top:336px;">• Skill 4 goes here</p>
  <p class="skill abs" style="left:572px;top:258px;">• Skill 5 goes here</p>
  <p class="skill abs" style="left:572px;top:284px;">• Skill 6 goes here</p>
  <p class="skill abs" style="left:572px;top:310px;">• Skill 7 goes here</p>
  <p class="skill abs" style="left:572px;top:336px;">• Skill 8 goes here</p>

  <!-- Referees -->
  <h2 class="heading lg abs" style="left:434px;top:369px;">REFEREES</h2>
  <p class="ref-label abs" style="left:434px;top:406px;">Referee Name</p>
  <div class="ref-line abs" style="left:434px;top:441px;"></div>
  <p class="ref-label abs" style="left:434px;top:453px;">Position, Relationship</p>
  <div class="ref-line abs" style="left:434px;top:488px;"></div>
  <p class="ref-label abs" style="left:434px;top:503px;">Contact ph</p>
  <div class="ref-line abs" style="left:437px;top:540px;"></div>
  <p class="ref-label abs" style="left:434px;top:555px;">Email</p>
  <div class="ref-line abs" style="left:434px;top:589px;"></div>

  <!-- Continuing education -->
  <h2 class="heading abs" style="left:414px;top:618px;font-size:14.5px;">CONTINUING EDUCATION</h2>
  <p class="col-label abs" style="left:390px;top:654px;line-height:21px;">Qualification<br>title</p>
  <p class="col-label abs" style="left:504px;top:654px;line-height:21px;">Institution</p>
  <p class="col-label abs" style="left:639px;top:654px;line-height:21px;">Year<br>completed</p>
  <div class="bar blue abs" style="left:340px;top:706px;"></div>
  <div class="bar teal abs" style="left:466px;top:706px;"></div>
  <div class="bar blue abs" style="left:590px;top:706px;"></div>

  <!-- About / experience -->
  <section class="about abs">
    <h2 class="panel-heading abs" style="left:27px;top:33px;">ABOUT ME</h2>
    <p class="panel-text abs" style="left:26px;top:70px;width:238px;">Lorem Ipsum is simply dummy text of the printing and typesetting industry. Lorem Ipsum has been the industry's standard dummy text ever since the 1500s, when an unknown printer took a galley of type and scrambled it to make a type specimen book.</p>
    <h2 class="panel-heading abs" style="left:27px;top:224px;">PROFESSIONAL<br>EXPERIENCE</h2>
    <ul class="experience abs" style="left:26px;top:288px;">
      <li>Experience 1</li>
      <li>Experience 2</li>
      <li>Experience 3</li>
      <li>Experience 4</li>
    </ul>
  </section>

  <!-- Interests -->
  <section class="interests abs">
    <h2 class="panel-heading abs" style="left:27px;top:35px;">PERSONAL INTERESTS AND<br>ACHIEVEMENTS</h2>
    <p class="panel-text abs" style="left:27px;top:103px;width:372px;">Lorem Ipsum is simply dummy text of the printing and typesetting industry. Lorem Ipsum has been the industry's standard dummy text ever since the 1500s, been the been industry's standard dummy text ever since the 1500s, Lorem Ipsum is simply dummy text of the printing and typesetting industry. Lorem Ipsum has been the industry's standard dummy text ever since the 1500s, been the been industry's standard dummy text ever since the 1500s,</p>
  </section>

</main>
</body>
</html>
```